Black Hair Stylist Business Card

Looking a for a business card for my hair styling business. Would like the card to be clean and giving our company a sophisticated look. I specialize in black hair styling including braids, sew ins and extensions. I have uploaded two versions of my logo, both are PNG files.

On the front of the card I would like my logo, name (Marisol Quenby), phone number (Will provide number to the winner, for now use a fake number) and the area I service which is Larkmere, OR.

On the back I would like a list of the different styles of hair I do.
Knotless Braids - Feeding Braids - Bohemian Braids - Extensions - Sew In - Crochet - Butterfly Locs - Twist

On the back I would also like to note I have great reviews. Would be nice to have 5 Stars Emojis - TressNook I may also provide a QR code to take customers to my TressNook Page.

PLEASE NOTE: Originally I upload 2 versions of our logo. Now that we've seen some options we've decided to go with the pink logo and a white/cream white background.

Target Market(s)

Black Men and Women

Industry/Entity Type

Hair Styling and Design

Contact Information for Business Card

Please refer to the Project Description for details.

Font styles to use
Serif
Sans Serif

Colors
E54698
E96AAD
F1A4CE
F9D9EA
FCEFF6
A7469A
B969AE
D3A5CF
EDDBEB
F8F0F9

Requirements
Must have
• Please refer to the Project Description for details.
Nice to have
• Easy to read and feels sophisticated.
Should not have
• Should not be too busy looking.

```html
<!DOCTYPE html>
<html lang="en">
<head>
<meta charset="utf-8">
<title>Marisol Quenby — Business Card</title>
<link href="https://fonts.googleapis.com/css2?family=Dancing+Script:wght@600&family=Montserrat:wght@500;700;800&display=swap" rel="stylesheet">
<style>
  :root {
    --backdrop: #e4e4e4;
    --card: #f7f2e9;
    --pink: #e5197f;
    --purple: #b23fd6;
    --ink: #232323;
    --ghost: #ebe5da;
    --pill: #ffffff;
    --divider: #999999;
    --star: #f6a81a;
  }
  * { box-sizing: border-box; margin: 0; padding: 0; }
  html, body { width: 1200px; height: 1000px; overflow: hidden; }
  body {
    background: var(--backdrop);
    font-family: "Montserrat", sans-serif;
    position: relative;
  }
  .card {
    position: absolute;
    width: 525px;
    height: 300px;
    border-radius: 26px;
    background: var(--card);
    box-shadow: 0 18px 40px rgba(0,0,0,0.14);
    overflow: hidden;
  }
  .card--back { left: 90px; top: 210px; }
  .card--front { left: 585px; top: 490px; }

  /* back */
  .brand {
    position: absolute; left: 60px; top: 92px;
    display: flex; align-items: center; gap: 10px;
    color: var(--pink);
    font-weight: 800;
    font-size: 26px;
    line-height: 1;
  }
  .brand-dot { width: 14px; height: 14px; border-radius: 50%; background: var(--pink); }
  .brand-sub {
    position: absolute; left: 84px; top: 124px;
    color: var(--pink); font-weight: 800; font-size: 10px; letter-spacing: 2.5px;
  }
  .reviews {
    position: absolute; right: 70px; top: 72px;
    text-align: center;
  }
  .reviews-name { font-weight: 800; font-size: 30px; color: var(--ink); letter-spacing: -0.5px; }
  .stars { display: flex; justify-content: center; gap: 5px; margin-top: 8px; }
  .stars svg { width: 18px; height: 18px; fill: var(--star); }
  .services {
    position: absolute; left: 50px; bottom: 54px; right: 40px;
    font-weight: 700; font-size: 15px; line-height: 1.3; color: var(--ink);
  }

  /* front */
  .mark-ghost {
    position: absolute; right: 40px; top: -40px;
    width: 230px; height: 230px; border-radius: 50%;
    background: var(--ghost);
  }
  .identity { position: absolute; left: 0; right: 0; top: 128px; text-align: center; }
  .name {
    font-family: "Dancing Script", cursive;
    font-weight: 600; font-size: 50px; color: var(--pink); line-height: 1;
  }
  .role { font-weight: 800; font-size: 17px; color: var(--purple); margin-top: 2px; padding-left: 60px; }
  .contact {
    position: absolute; left: 80px; right: 80px; bottom: 40px; height: 42px;
    background: var(--pill); border-radius: 21px;
    display: flex; align-items: center; justify-content: center; gap: 18px;
    font-weight: 500; font-size: 16px; color: var(--ink);
  }
  .contact-item { display: flex; align-items: center; gap: 8px; }
  .contact-item svg { width: 17px; height: 17px; }
  .contact-divider { width: 1px; height: 24px; background: var(--divider); }
</style>
</head>
<body>

<section class="card card--back" aria-label="Card back">
  <div class="brand"><span class="brand-dot"></span>Seraphine</div>
  <div class="brand-sub">BRAIDS &amp; EXTENSIONS</div>

  <div class="reviews">
    <div class="reviews-name">TressNook</div>
    <div class="stars" aria-label="Five star rating">
      <svg viewBox="0 0 24 24"><path d="M12 2l3 6.9 7.5.7-5.7 5 1.7 7.4L12 18.3 5.5 22l1.7-7.4-5.7-5 7.5-.7z"/></svg>
      <svg viewBox="0 0 24 24"><path d="M12 2l3 6.9 7.5.7-5.7 5 1.7 7.4L12 18.3 5.5 22l1.7-7.4-5.7-5 7.5-.7z"/></svg>
      <svg viewBox="0 0 24 24"><path d="M12 2l3 6.9 7.5.7-5.7 5 1.7 7.4L12 18.3 5.5 22l1.7-7.4-5.7-5 7.5-.7z"/></svg>
      <svg viewBox="0 0 24 24"><path d="M12 2l3 6.9 7.5.7-5.7 5 1.7 7.4L12 18.3 5.5 22l1.7-7.4-5.7-5 7.5-.7z"/></svg>
      <svg viewBox="0 0 24 24"><path d="M12 2l3 6.9 7.5.7-5.7 5 1.7 7.4L12 18.3 5.5 22l1.7-7.4-5.7-5 7.5-.7z"/></svg>
    </div>
  </div>

  <p class="services">Knotless Braids • Feeding Braids • Bohemian Braids<br>Extensions • Sew In • Crochet • Butterfly Locs • Twist</p>
</section>

<section class="card card--front" aria-label="Card front">
  <div class="mark-ghost"></div>
  <div class="identity">
    <h1 class="name">Marisol Quenby</h1>
    <p class="role">Black Hair Stylist</p>
  </div>
  <div class="contact">
    <span class="contact-item">
      <svg viewBox="0 0 24 24"><path fill="#222" d="M6.6 10.8a15.1 15.1 0 0 0 6.6 6.6l2.2-2.2a1 1 0 0 1 1-.25 11.4 11.4 0 0 0 3.6.6 1 1 0 0 1 1 1V20a1 1 0 0 1-1 1A17 17 0 0 1 3 4a1 1 0 0 1 1-1h3.5a1 1 0 0 1 1 1c0 1.25.2 2.450.6 3.6a1 1 0 0 1-.25 1z"/></svg>
      555-204-7316
    </span>
    <span class="contact-divider"></span>
    <span class="contact-item">
      <svg viewBox="0 0 24 24" fill="none" stroke="#222" stroke-width="2"><path d="M12 22s7-7 7-12a7 7 0 0 0-14 0c0 5 7 12 7 12z"/><circle cx="12" cy="10" r="2.5"/></svg>
      Larkmere, OR
    </span>
  </div>
</section>

</body>
</html>
```